Kambo Flyer

to create a Flyer with information about Kambo Ceremonies. The flyer that is up loaded is an example

Requirements
Must have
• Benefits of Kambo
• Kambo is traditionally known to be anti-inflammatory, to relieve joint pain, to heal eyesight, and to ease pain. Kambo peptides, and their effects, are reported to cover a wide range of potential medical uses: treatment of brain diseases such as Alzheimer’s and Parkinson’s, depression, migraines, blood circulation problems, vascular insufficiency, organ diseases, skin and eyes issues, cancer, fertility problems in women, AIDS, candida, hepatitis, herpes, and more
• What is Kambo
• The scientific name for this frog is Phyllomedusa bicolor or “Two-Colored Leaf Guardian.” It is also known as the “Giant Green Monkey Tree Frog.”
• Kambo is legal in the United States, as well as all other countries, and is not a hallucinogenic. It is, however, a deep cleansing therapy – – physically, emotionally and mentally. It is one of the world’s most effective and natural antibiotics and immune system boosters. It detoxifies the liver and intestines, improves mental functioning, and has the potential to dissolve emotional blocks. It also helps to reset our cellular memory.
• Please note that fasting 12 hours prior to the ceremony is required
• Private (in Home} Semi-Private and Group Ceremonies Available
• For More information see our website
• www.MeadowLightHalls.org
• 555-214-0873
• Traditional Shamanic Kambo Ceremonies in Florida

```html
<!DOCTYPE html>
<html lang="en">
<head>
<meta charset="utf-8">
<title>Traditional Shamanic Kambo Ceremonies in Florida</title>
<link rel="stylesheet" href="https://fonts.googleapis.com/css2?family=Mulish:ital,wght@0,400;0,700;0,800;1,500&family=Didact+Gothic&display=swap">
<style>
:root{
  --black:#000;
  --white:#fff;
  --leaf:#8fbf7a;
  --band:#a6d08d;
  --gold:#f5e21a;
  --sun:#f7c01d;
  --ink:#1b1b1b;
  --panel-top:#ffffff;
  --panel-mid:#e3e3e3;
  --panel-low:#c9c9c9;
  --brand:#5d7a4a;
}
*{margin:0;padding:0;box-sizing:border-box}
html,body{width:1137px;height:1200px;overflow:hidden;background:var(--black)}
.flyer{position:relative;width:1137px;height:1200px;background:var(--black);overflow:hidden;font-family:"Didact Gothic",sans-serif;color:var(--white)}
.team-panel{position:absolute;left:846px;top:0;width:291px;height:1200px;background:linear-gradient(180deg,var(--panel-top) 0%,var(--panel-mid) 45%,var(--panel-low) 75%,var(--panel-mid) 100%)}
.headline{position:absolute;left:81px;top:70px;font-family:"Mulish",sans-serif;font-weight:800;font-size:33px;line-height:43px;color:var(--white)}
.headline .accent{color:var(--leaf)}
.section-title{position:absolute;left:83px;font-family:"Mulish",sans-serif;font-weight:800;font-size:19px;color:var(--gold)}
.benefits-title{top:180px}
.kambo-title{top:427px}
.copy{position:absolute;font-size:19px;line-height:24.3px;letter-spacing:.1px}
.benefits-copy{left:83px;top:213px;width:681px;text-align:justify}
.species-copy{left:83px;top:460px;width:681px;text-align:justify}
.about-copy{left:285px;top:528px;width:479px;font-size:16.4px;line-height:21.8px;text-align:justify}
.photo{position:absolute;border:5px solid var(--white)}
.ritual-photo{left:580px;top:40px;width:330px;height:200px;transform:rotate(-27deg);background:radial-gradient(circle at 75% 35%,#5a9a30 0%,#7a3a16 35%,#3a1a0c 70%,#1a0a05 100%)}
.ritual-art{left:-5px;top:535px;width:260px;height:166px;background:linear-gradient(120deg,#f0e0c8 0%,#e07a30 40%,#8a3a1a 70%,#6fa83a 100%)}
.frog-photo{position:absolute;left:250px;top:800px;width:596px;height:400px;background:radial-gradient(ellipse at 55% 30%,#4fd63a 0%,#2a9a1e 30%,#10300c 60%,#000 85%)}
.notes{position:absolute;left:83px;top:727px;list-style:none;font-family:"Mulish",sans-serif;font-style:italic;font-weight:500;font-size:19.5px;line-height:24px;color:var(--gold)}
.notes li{padding-left:34px;position:relative}
.notes li::before{content:"";position:absolute;left:2px;top:9px;width:7px;height:7px;border-radius:50%;background:var(--gold)}
.info-band{position:absolute;left:0;top:998px;width:846px;height:42px;background:var(--band)}
.info-band span{position:absolute;left:349px;top:9px;font-family:"Mulish",sans-serif;font-weight:800;font-size:19px;color:var(--ink)}
.website{position:absolute;left:349px;top:1047px;font-family:"Mulish",sans-serif;font-weight:800;font-size:19px;color:var(--white)}
.call-badge{position:absolute;left:40px;top:880px;width:280px;height:280px;border-radius:50%;background:var(--sun);color:var(--ink);text-align:center}
.call-badge svg{position:absolute;left:0;top:0}
.call-label{position:absolute;left:0;right:0;top:80px;font-family:"Mulish",sans-serif;font-weight:800;font-size:35px}
.call-number{position:absolute;left:0;right:0;top:122px;font-family:"Mulish",sans-serif;font-size:35px;font-weight:400}
.badge-brand{position:absolute;left:0;right:0;top:192px;font-family:"Mulish",sans-serif;font-weight:700;font-size:14px;color:#6a5a20}
.member{position:absolute;left:846px;width:291px;text-align:center;color:var(--ink)}
.portrait{width:146px;height:146px;margin:0 auto 8px;border-radius:50%;border:4px solid #8d8d8d}
.member .name{font-family:"Mulish",sans-serif;font-weight:800;font-size:19px;line-height:23px}
.member .role{font-size:17px;line-height:21.5px}
.m1{top:218px}.m1 .portrait{background:linear-gradient(160deg,#3a3a3a,#8a6a55)}
.m2{top:464px}.m2 .portrait{background:linear-gradient(160deg,#fff,#d9b77a)}
.m3{top:711px}.m3 .portrait{background:radial-gradient(circle at 25% 30%,#ff8a2a,#3a1a10 60%,#111)}
.panel-brand{position:absolute;left:846px;width:291px;top:1082px;text-align:center;font-family:"Mulish",sans-serif;font-weight:700;font-size:24px;color:var(--brand)}
</style>
</head>
<body>
<main class="flyer">
  <aside class="team-panel"></aside>

  <div class="photo ritual-photo" role="img" aria-label="Practitioner applying kambo with a wooden stick, glowing tree frog artwork"></div>

  <h1 class="headline">Traditional <span class="accent">Shamanic Kambo</span><br>Ceremonies in Florida</h1>

  <h2 class="section-title benefits-title">Benefits of Kambo</h2>
  <p class="copy benefits-copy">Kambo is traditionally known to be anti-inflammatory,<br>to relieve joint pain, to heal eyesight, and to ease pain.<br>Kambo peptides, and their effects, are reported to cover<br>a wide range of potential medical uses: treatment of brain<br>diseases such as Alzheimer’s and Parkinson’s, depression, migraines, blood circulation problems, vascular insufficiency, organ diseases, skin and eyes issues, cancer, fertility problems in women, AIDS, candida, hepatitis, herpes, and more</p>

  <h2 class="section-title kambo-title">What is Kambo</h2>
  <p class="copy species-copy">The scientific name for this frog is Phyllomedusa bicolor or “Two-Colored Leaf Guardian.” It is also known as the “Giant Green Monkey Tree Frog.”</p>

  <div class="photo ritual-art" role="img" aria-label="Painted illustration of kambo being applied to a shoulder beside a tree frog"></div>
  <p class="copy about-copy">Kambo is legal in the United States, as well as all other countries, and is not a hallucinogenic. It is, however, a deep cleansing therapy – – physically, emotionally and mentally. It is one of the world’s most effective and natural antibiotics and immune system boosters. It detoxifies the liver and intestines, improves mental functioning, and has the potential to dissolve emotional blocks. It also helps to reset our cellular memory.</p>

  <ul class="notes">
    <li>Please note that fasting 12 hours prior to the ceremony is required</li>
    <li>Private (in Home} Semi-Private and Group Ceremonies Available</li>
  </ul>

  <div class="frog-photo" role="img" aria-label="Photograph of a giant green monkey tree frog on a branch"></div>

  <div class="info-band"><span>For More information see our website</span></div>
  <div class="website">www.MeadowLightHalls.org</div>

  <div class="call-badge">
    <svg width="280" height="280" viewBox="0 0 280 280" aria-hidden="true">
      <path d="M40 70 A125 125 0 0 1 240 70" fill="none" stroke="#1b1b1b" stroke-width="3"/>
      <path d="M40 210 A125 125 0 0 0 240 210" fill="none" stroke="#1b1b1b" stroke-width="3"/>
    </svg>
    <div class="call-label">CALL US</div>
    <div class="call-number">555-214-0873</div>
    <div class="badge-brand">Meadow Light Halls</div>
  </div>

  <div class="member m1">
    <div class="portrait" role="img" aria-label="Portrait of Dan Hollis"></div>
    <div class="name">Dan Hollis</div>
    <div class="role">Founder<br>Practitioner of Kambo</div>
  </div>
  <div class="member m2">
    <div class="portrait" role="img" aria-label="Portrait of Mara Quinlan"></div>
    <div class="name">Mara Quinlan</div>
    <div class="role">Kambo Practitioner</div>
  </div>
  <div class="member m3">
    <div class="portrait" role="img" aria-label="Portrait of Theo Barrick by a fire"></div>
    <div class="name">Theo Barrick</div>
    <div class="role">Fire Keeper and Facilitator</div>
  </div>

  <div class="panel-brand">Meadow Light Halls</div>
</main>
</body>
</html>
```